Pet Shop Website

website will need to have the following features:
• Photo Galleries of each species (Dogs, Cats, Birds, Fish, Reptiles, Rabbits) in a light box popup
o Each species may have several different categories for example:
 Fish
• Marine fish
• Fresh water
• tropical
• Cichlid
• Information Fact sheets of each species – Downloaded as a pdf which can be either
o Care Sheets
o Training Sheets
• Members Area
o Username (Email Address) & Password login
o New signups
o Exclusive Member Deals
o Newsletter options

The front page must be very simple (for example lumavest.com.au) contain the following:
• Product of the week - which can be purchased online
o Short details
o Cost
• Pet Club Sign up picture
• Animal of the week/month
• Contact Phone Number and addresses of the stores
• A jQuery slideshow (Images could include stores, pets etc…)
The main page MUST keep simple. We do not want it cluttered.

Inner Page
The animals / reptile page will need to have:
• Short description of the species
• Photo Galleries
• A list of what is in stock and the list needs to clearly be sorted by each store (Use of Tabs maybe).
• Facts sheets / Info sheets
The type of website ideas (not the type of look that we are necessary after) is and the sort of content that we want to offer are as follows:

http://www.scalenook.com.au/
http://www.brindlecovepaws.com.au/
http://www.thefurrowden.com.au
http://www.tailtown.net.au

Colour in the new website:
Blue
Red
Grey
Yellow

Original site:

http://www.critterglow.com.au
Updates

Hi Guys,

We had feedback from the client and they would like to see a few dark designs.

Thanks                                   

Reason: We would like to reopen this contest back up for a further week

Target Market(s)

Targeting animal lovers

Industry/Entity Type

Store

Requirements
Should not have
• Alter the logo in anyway

```html
<!DOCTYPE html>
<html lang="en">
<head>
<meta charset="utf-8">
<title>Critter Glow – Pet Shop</title>
<link rel="stylesheet" href="https://fonts.googleapis.com/css2?family=Cabin:wght@400;500;700&family=Arimo:wght@400;700&family=Arvo:wght@700&display=swap">
<style>
  :root{
    --orange:#fda00f;
    --orange-deep:#f88a05;
    --heading-orange:#f7a11a;
    --soft-yellow:#f3d36c;
    --navy:#050a3d;
    --panel:#1a1f6b;
    --red:#b80f12;
    --white:#ffffff;
    --ink:#1b1f5e;
  }
  *{box-sizing:border-box;margin:0;padding:0}
  html,body{width:1200px;height:1200px;overflow:hidden}
  body{position:relative;background:var(--navy);font-family:"Arimo",Arial,sans-serif;color:var(--white)}
  .abs{position:absolute}

  .top-bar{left:0;top:0;width:1200px;height:48px;background:var(--orange);border-bottom:2px solid var(--white)}
  .main-nav{right:54px;top:12px;display:flex;gap:0;font-family:"Cabin",sans-serif;font-size:18px;color:var(--navy)}
  .main-nav span{padding:0 12px}
  .main-nav .sep{padding:0}
  .main-nav .current{color:var(--white);font-weight:500}

  .brand-box{left:46px;top:0;width:276px;height:107px;background:var(--white);border-radius:0 0 4px 4px;box-shadow:0 2px 6px rgba(0,0,0,.4);display:flex;align-items:center;justify-content:center;gap:10px}
  .brand-box .dot{width:18px;height:18px;background:var(--ink);border-radius:50%}
  .brand-name{font-family:"Cabin",sans-serif;font-weight:700;font-size:30px;color:var(--ink)}

  .hero{left:0;top:50px;width:1200px;height:368px;background:linear-gradient(90deg,#4e6a22 0%,#7b8f3a 40%,#a46f3a 60%,#5f7a2c 100%);z-index:-1}
  .slide-dots{left:1080px;top:387px;display:flex;gap:13px}
  .slide-dots i{width:13px;height:13px;border-radius:50%;background:var(--orange);border:2px solid var(--orange)}
  .slide-dots i.empty{background:transparent}
  .hero-rule{left:0;top:418px;width:1200px;height:2px;background:var(--orange)}

  .feature-panel{left:23px;top:437px;width:1152px;height:266px;background:var(--panel)}
  .feature-photo{left:48px;top:469px;width:306px;height:203px;border:2px solid var(--white);background:linear-gradient(135deg,#2e4a1c,#6fa03a 55%,#cfd3c4)}
  .feature-title{left:398px;top:472px;font-family:"Cabin",sans-serif;font-size:56px;line-height:58px;color:var(--heading-orange)}
  .feature-name{left:398px;top:607px;font-family:"Cabin",sans-serif;font-size:29px;color:var(--soft-yellow)}
  .feature-copy{left:752px;top:485px;width:379px;font-size:15.5px;line-height:21.5px;text-align:justify}
  .feature-price{left:752px;top:581px;font-family:"Cabin",sans-serif;font-size:21px;color:var(--soft-yellow)}
  .feature-price b{margin-left:14px;font-weight:500}
  .btn-buy{left:754px;top:624px;width:86px;height:36px;background:var(--orange);color:var(--navy);border-radius:3px;font-family:"Cabin",sans-serif;font-size:18px;display:flex;align-items:center;justify-content:center;box-shadow:1px 2px 3px rgba(0,0,0,.5)}

  .club-card{left:46px;top:734px;width:398px;height:294px;background:var(--orange);border-radius:3px;overflow:hidden}
  .club-card h2{height:51px;background:var(--orange-deep);font-family:"Arvo",serif;font-size:21px;color:var(--navy);text-align:center;line-height:51px;letter-spacing:.5px}
  .field-label{left:68px;font-size:16px;color:var(--navy)}
  .field{left:179px;width:236px;height:30px;background:var(--white);border-radius:3px;font-size:15px;color:#a7a7a7;padding:6px 6px}
  .btn-submit{left:178px;top:926px;width:127px;height:44px;background:var(--red);border-radius:3px;font-weight:700;font-size:18px;display:flex;align-items:center;justify-content:center;box-shadow:1px 2px 3px rgba(0,0,0,.4)}

  .col-heading{font-weight:700;font-size:18px;color:var(--heading-orange);padding-bottom:8px;border-bottom:1px solid var(--heading-orange)}
  .month-heading{left:566px;top:733px;width:218px;text-align:center}
  .month-photo{left:583px;top:790px;width:189px;height:140px;border:2px solid var(--white);background:linear-gradient(160deg,#3d5a2a,#9a4a3a 45%,#e8e8e8 60%,#4a6030)}
  .month-copy{left:554px;top:961px;width:268px;font-size:15.5px;line-height:21.5px;text-align:justify;height:64px;overflow:hidden}

  .store-heading{left:918px;top:731px;width:164px}
  .store-list{left:918px;top:781px;font-size:16.5px;line-height:26.4px}
  .store-list b{font-size:17px}
  .store-list .gap{height:26.4px}

  .footer-rule{left:0;top:1062px;width:1200px;height:2px;background:var(--orange)}
  .footer-heading{font-family:"Cabin",sans-serif;font-weight:500;font-size:23px;color:var(--heading-orange)}
  .newsletter-heading{left:49px;top:1076px}
  .newsletter-field{left:47px;top:1114px;width:285px;height:29px;background:var(--white);border-radius:2px;color:#777;font-size:17px;padding:4px 10px}
  .btn-subscribe{left:356px;top:1112px;width:116px;height:35px;background:var(--red);border-radius:2px;font-size:18px;font-weight:500;display:flex;align-items:center;justify-content:center}
  .follow-heading{left:560px;top:1078px}
  .social-links{left:560px;top:1113px;display:flex;gap:6px}
  .social-links i{width:34px;height:34px;border-radius:50%;background:#f3c275;border:2px solid #d6d6d6}
  .copyright{right:35px;top:1155px;font-size:13px}
</style>
</head>
<body>
  <div class="abs hero" role="img" aria-label="Slideshow photo of a beagle puppy beside a crested songbird on a green background"></div>
  <div class="abs slide-dots"><i class="empty"></i><i></i><i></i></div>
  <div class="abs hero-rule"></div>

  <header class="abs top-bar"></header>
  <div class="abs brand-box"><span class="dot"></span><span class="brand-name">Critter Glow</span></div>
  <nav class="abs main-nav">
    <span class="current">Home</span><span class="sep">|</span>
    <span>Shop</span><span class="sep">|</span>
    <span>Pets</span><span class="sep">|</span>
    <span>Events</span><span class="sep">|</span>
    <span>Gallery</span><span class="sep">|</span>
    <span>About</span><span class="sep">|</span>
    <span style="padding-right:0">Contact us</span>
  </nav>

  <section class="abs feature-panel"></section>
  <div class="abs feature-photo" role="img" aria-label="Product photo of a green iguana on a rock"></div>
  <h1 class="abs feature-title" style="font-weight:400">Product<br>of the week</h1>
  <div class="abs feature-name">Name of the product</div>
  <p class="abs feature-copy">Lorem ipsum dolor sit amet, vel ne quidam patrio&shy;que dissentiunt, cum ad suas omnes dicant. Ex sed augue albucius appellantur, ne nec solet ubique disputando.</p>
  <div class="abs feature-price">Price <b>$ 200</b></div>
  <div class="abs btn-buy">Buy now</div>

  <section class="abs club-card"><h2>PET CLUB SIGN UP</h2></section>
  <div class="abs field-label" style="top:818px">Username</div>
  <div class="abs field" style="top:815px">Email id</div>
  <div class="abs field-label" style="top:866px">Password</div>
  <div class="abs field" style="top:858px">Password</div>
  <div class="abs btn-submit">SUBMIT</div>

  <h3 class="abs col-heading month-heading">ANIMAL OF THE MONTH</h3>
  <div class="abs month-photo" role="img" aria-label="Photo of a white rabbit among red flowers"></div>
  <p class="abs month-copy">Lorem ipsum dolor sit amet, vel ne quidam patrioque dissentiunt, cum ad suas omnes dicant. Ex sed augue albucius.</p>

  <h3 class="abs col-heading store-heading">STORE LOCATION</h3>
  <address class="abs store-list" style="font-style:normal">
    Shop 3 / 420 Marlow Hwy<br>
    ASHGROVE W.A 6109<br>
    <b>Phone: (08) 9555 0142</b><br>
    <b>Fax: (08) 9555 0143</b>
    <div class="gap"></div>
    Unit 2 / 18 Harbour Drive<br>
    REEDVALE W.A 6165<br>
    <b>Phone: (08) 9555 0178</b><br>
    <b>Fax: (08) 9555 0179</b>
  </address>

  <div class="abs footer-rule"></div>
  <h3 class="abs footer-heading newsletter-heading">Newsletter Sign up</h3>
  <div class="abs newsletter-field">email id</div>
  <div class="abs btn-subscribe">Subscribe</div>
  <h3 class="abs footer-heading follow-heading">Follow us</h3>
  <div class="abs social-links"><i aria-label="Social link"></i><i aria-label="Social link"></i></div>
  <div class="abs copyright">Copyright 2012 Critter Glow. All rights reserved.</div>
</body>
</html>
```